Business card design and logo needed - Photographer

I take photos of weddings, rodeos, snowmobiling.
Need a card to hand out to prospective clients.
Industry/Entity Type
Business
Contact Information for Business Card
Marcus Dolven Photography
Requirements
Must have
- Bold
Black or white base.
My website. www.MarcusDolven.example
Should not have
- camera/ lens/ aperture blades

```html
<!DOCTYPE html>
<html lang="en">
<head>
<meta charset="utf-8">
<title>Marcus Dolven Photography – Business Card</title>
<link rel="stylesheet" href="https://fonts.googleapis.com/css2?family=Nunito+Sans:wght@300;400;600&display=swap">
<style>
  :root {
    --backdrop: #e4e8ea;
    --card-dark: #070908;
    --card-light: #ffffff;
    --ink-light: #ffffff;
    --ink-dark: #0a0a0a;
  }
  * { margin: 0; padding: 0; box-sizing: border-box; }
  html, body {
    width: 1200px;
    height: 900px;
    overflow: hidden;
    background: var(--backdrop);
  }
  .canvas {
    position: relative;
    width: 1200px;
    height: 900px;
  }
  .business-card {
    position: absolute;
    left: 322px;
    top: 304px;
    width: 578px;
    height: 333px;
    display: flex;
    font-family: "Nunito Sans", "Helvetica Neue", Arial, sans-serif;
  }
  .card-info {
    position: relative;
    width: 360px;
    height: 100%;
    background: var(--card-dark);
    color: var(--ink-light);
  }
  .studio-name {
    position: absolute;
    left: 43px;
    top: 195px;
    font-size: 21px;
    font-weight: 300;
    letter-spacing: 0.2px;
    white-space: nowrap;
  }
  .contact-list {
    position: absolute;
    left: 43px;
    top: 238px;
    list-style: none;
    font-size: 14.5px;
    font-weight: 400;
    line-height: 18.5px;
    white-space: nowrap;
  }
  .card-brand {
    position: relative;
    flex: 1;
    height: 100%;
    background: var(--card-light);
    color: var(--ink-dark);
  }
  .brand-name {
    position: absolute;
    left: 28px;
    top: 195px;
    display: flex;
    align-items: center;
    gap: 8px;
    font-size: 19px;
    font-weight: 600;
    letter-spacing: 0.6px;
    white-space: nowrap;
  }
  .brand-mark {
    width: 8px;
    height: 8px;
    background: var(--ink-dark);
  }
</style>
</head>
<body>
  <main class="canvas">
    <article class="business-card">
      <section class="card-info">
        <h1 class="studio-name">Marcus Dolven Photography</h1>
        <ul class="contact-list">
          <li class="contact-phone">555.014.2290</li>
          <li class="contact-web">www.MarcusDolven.example</li>
          <li class="contact-social">www.social.example/marcus.dolven</li>
        </ul>
      </section>
      <section class="card-brand">
        <p class="brand-name"><span class="brand-mark"></span>MARCUS DOLVEN</p>
      </section>
    </article>
  </main>
</body>
</html>
```